Medical Practice Business Card

we need a business card for our new medical ophthalmology practice based in Needham Massachusetts. we are looking for a simple , modern and elegant design.
the card needs to contain the following
1- the logo of our practice (please see attached file)
2- the name of the practice : "Silver Birch Retina Care"
3- Doctor's Name: Tobias Rendell MD PhD
4- Specialty: Board-Certified Vitreoretinal Surgeon
5- practice address: 87 Larkspur Ave, Suite 210, Alder Falls AF 00481
7- Office number: 617- 482 - 7730
8- fax number: 617- 391 - 2268
9- email: info@sbretinahub.example
10- website: www.sbretinahub.example

```html
<!DOCTYPE html>
<html lang="en">
<head>
<meta charset="UTF-8">
<title>Silver Birch Retina Care – Business Card</title>
<link href="https://fonts.googleapis.com/css2?family=Arimo:wght@400;700&family=Cinzel:wght@700&display=swap" rel="stylesheet">
<style>
  :root {
    --backdrop: #7b7b7b;
    --navy: #17375e;
    --navy-deep: #14304f;
    --blue: #1f74b8;
    --paper: #f6f7f9;
    --ink: #1b1b1b;
    --white: #ffffff;
  }
  * { box-sizing: border-box; margin: 0; padding: 0; }
  html, body { width: 1200px; height: 900px; overflow: hidden; }
  body {
    background: var(--backdrop);
    font-family: "Arimo", Arial, sans-serif;
    position: relative;
  }
  .card {
    position: absolute;
    left: 280px;
    width: 640px;
    height: 366px;
    border-radius: 22px;
    overflow: hidden;
    box-shadow: 0 10px 28px rgba(0,0,0,0.35);
  }
  /* Front */
  .card-front {
    top: 60px;
    background: radial-gradient(ellipse at 50% 45%, #2e78b0 0%, #1f5286 45%, var(--navy-deep) 100%);
    color: var(--white);
  }
  .front-name {
    position: absolute;
    top: 150px; left: 0; right: 0;
    text-align: center;
    font-family: "Arimo", Arial, sans-serif;
    font-weight: 400;
    font-size: 40px;
    line-height: 1.2;
  }
  .front-web {
    position: absolute;
    top: 266px; left: 0; right: 0;
    text-align: center;
    font-size: 14px;
    letter-spacing: 4px;
  }
  /* Back */
  .card-back {
    top: 474px;
    background: var(--paper);
    color: var(--ink);
  }
  .back-brand {
    position: absolute;
    top: 48px; right: 40px;
    display: flex; align-items: center; gap: 12px;
  }
  .brand-dot {
    width: 14px; height: 14px; border-radius: 50%;
    background: var(--blue);
  }
  .brand-name {
    font-family: "Arimo", Arial, sans-serif;
    font-weight: 400;
    font-size: 24px;
    color: var(--navy);
  }
  .doctor {
    position: absolute;
    left: 40px; top: 196px;
  }
  .doctor-name {
    font-family: "Cinzel", Georgia, serif;
    font-weight: 700;
    font-size: 28px;
    color: var(--navy);
  }
  .doctor-title {
    font-size: 16px;
    color: var(--blue);
    padding-bottom: 8px;
    border-bottom: 1px solid var(--ink);
    width: 360px;
  }
  .phones { margin-top: 8px; font-size: 16px; line-height: 1.4; }
  .phones li { list-style: none; display: flex; align-items: center; gap: 8px; }
  .phones svg { width: 14px; height: 14px; fill: var(--navy); }
  .contact {
    position: absolute;
    right: 40px; top: 140px;
    text-align: right;
    font-size: 15px;
    line-height: 1.35;
    font-style: normal;
  }
  .contact-email {
    padding-bottom: 6px;
    border-bottom: 1px solid var(--ink);
    margin-bottom: 6px;
  }
  .back-bands { position: absolute; left: 0; top: 0; width: 640px; height: 366px; }
  .back-web {
    position: absolute;
    right: 40px; bottom: 34px;
    color: var(--white);
    font-size: 15px;
  }
</style>
</head>
<body>
  <section class="card card-front">
    <h1 class="front-name">Silver Birch Retina Care</h1>
    <p class="front-web">www.sbretinahub.example</p>
  </section>

  <section class="card card-back">
    <svg class="back-bands" viewBox="0 0 640 366" aria-hidden="true">
      <polygon points="0,322 372,322 392,292 404,292 380,344 0,344" fill="#17375e"/>
      <polygon points="404,292 640,292 640,366 0,366 0,350 386,350" fill="#1f74b8"/>
    </svg>

    <div class="back-brand">
      <span class="brand-dot"></span>
      <span class="brand-name">Silver Birch Retina Care</span>
    </div>

    <div class="doctor">
      <h2 class="doctor-name">Tobias Rendell MD PhD</h2>
      <p class="doctor-title">Board-Certified Vitreoretinal Surgeon</p>
      <ul class="phones">
        <li>
          <svg viewBox="0 0 24 24"><path d="M6.6 10.8a15.1 15.1 0 0 0 6.6 6.6l2.2-2.2a1 1 0 0 1 1-.25 11.4 11.4 0 0 0 3.6.57 1 1 0 0 1 1 1V20a1 1 0 0 1-1 1A17 17 0 0 1 3 4a1 1 0 0 1 1-1h3.5a1 1 0 0 1 1 1c0 1.25.2 2.45.57 3.57a1 1 0 0 1-.25 1z"/></svg>
          617- 482 - 7730
        </li>
        <li>
          <svg viewBox="0 0 24 24"><path d="M7 3h10v5H7z"/><path d="M4 9h16a1 1 0 0 1 1 1v8h-3v3H6v-3H3v-8a1 1 0 0 1 1-1zm4 8v2h8v-4H8z"/></svg>
          617- 391 - 2268
        </li>
      </ul>
    </div>

    <address class="contact">
      <p class="contact-email">info@sbretinahub.example</p>
      <p>87 Larkspur Ave, Suite 210</p>
      <p>Alder Falls AF 00481</p>
    </address>

    <p class="back-web">www.sbretinahub.example</p>
  </section>
</body>
</html>
```